Australian Real Estate Sales Consultant needs web design please.

I am a female residential real estate sales consultant for a large australian real estate franchise.
I need a web design for "wordpress" that contains an area that will accommodate my photo and details and company logo.
A large area that contains a feature property where images are on something like a slide show.
Tabs or something similar with images for Selling, Sold, Photography and News where people can look at listings but I do not want people to be able to post a comment.
Reason: Need more designers, may be forced to change to wordpress and offer more money.
Reason: Sorry for the delay, I have been concentrating on another project which I needed completed. I am now able to focus on my web design project and hope to have it all set up in the next 10 days as it is a high priority for me. Thank you for your patience and I will begin providing feedback to your designs shortly. Thanks, Marisha.
Target Market(s)
Potential sellers or purchasers of residential property
Industry/Entity Type
Residential
Requirements
Must have
- Ease of changing property photos and info
Nice to have
- Bright attractive colours

```html
<!DOCTYPE html>
<html lang="en">
<head>
<meta charset="utf-8">
<title>Marisha Ashcombe – Real Estate Consultant</title>
<link rel="stylesheet" href="https://fonts.googleapis.com/css2?family=Questrial&family=Noto+Serif&family=Arimo:wght@400;700&display=swap">
<style>
:root{
  --purple-light:#c59ee3;
  --purple:#a878cf;
  --purple-deep:#8a55b6;
  --purple-text:#7a3fa8;
  --page:#efefef;
  --panel:#ffffff;
  --line:#dedede;
  --ink:#2a2a2a;
  --muted:#8a8a8a;
  --link-blue:#1d4f9a;
  --price-red:#c8372d;
  --read-red:#d0261e;
  --video-black:#141414;
}
*{box-sizing:border-box;margin:0;padding:0}
html,body{width:683px;height:1200px;overflow:hidden}
body{position:relative;background:var(--page);font-family:"Arimo",Arial,sans-serif;color:var(--ink)}
.abs{position:absolute}
/* header */
.site-header{left:0;top:0;width:683px;height:375px;background:linear-gradient(180deg,var(--purple-deep) 0,var(--purple-light) 4px,var(--purple) 60%,var(--purple-light) 100%);border-bottom:2px solid var(--purple-deep)}
.brand-name{left:30px;top:17px;font-family:"Questrial",sans-serif;font-size:23px;color:#fff;letter-spacing:.2px;white-space:nowrap}
.brand-role{left:31px;top:45px;font-family:"Questrial",sans-serif;font-size:10px;color:#f3e8fb;letter-spacing:3.3px;white-space:nowrap}
.video-cta{left:413px;top:14px;width:237px;height:57px;background:linear-gradient(#3a3a3a,var(--video-black) 50%);border-radius:6px;border:1px solid #555}
.video-cta .badge{left:9px;top:8px;width:40px;height:40px;border-radius:6px;background:linear-gradient(#eee,#9a9a9a)}
.video-cta .title{left:60px;top:11px;font-family:"Noto Serif",serif;font-size:13px;color:#fff;white-space:nowrap}
.video-cta .action{left:117px;top:35px;font-family:"Noto Serif",serif;font-size:11px;color:#ff2a22;white-space:nowrap}
.hero{left:30px;top:80px;width:623px;height:249px;border:3px solid var(--purple-deep);background:linear-gradient(180deg,#6fb2ea 0,#8dc3ee 30%,#a69a88 55%,#8c7a66 75%,#5d8a3a 100%)}
.hero-portrait{left:0;top:0;width:340px;height:243px;background:linear-gradient(180deg,#6cb0ea,#7aa6c8 60%,#2a2422)}
.main-nav{left:28px;top:339px;width:625px;height:26px;border-radius:4px;background:linear-gradient(#fafafa,#dcdcdc);display:block}
.main-nav a{position:absolute;top:8px;font-size:9.5px;color:#333;text-decoration:none;letter-spacing:.2px;white-space:nowrap}
.main-nav a.current{color:var(--purple-text)}
.main-nav .franchise{position:absolute;right:13px;top:3px;font-family:"Questrial",sans-serif;font-size:18px;color:var(--purple-text)}
/* content */
.content{left:27px;top:387px;width:625px;height:739px;background:var(--panel);border:1px solid var(--line)}
.section-title{font-family:"Noto Serif",serif;font-weight:400;font-size:13.5px;color:var(--ink);white-space:nowrap}
.arrow{width:13px;height:13px;border-radius:50%;background:linear-gradient(#fff,#ddd);border:1px solid #bbb}
.arrow svg{display:block}
.listing-row{left:40px;top:415px;width:596px;height:173px;border:1px solid var(--line);background:linear-gradient(#fff 70%,#f2f2f2)}
.listing{top:0;height:171px;width:198px}
.listing+.listing{border-left:1px solid var(--line)}
.listing .photo{left:20px;top:8px;width:152px;height:80px;background:linear-gradient(180deg,#2e6a2a,#9aa58a 45%,#d9dccf 70%,#4f8a35)}
.listing .price{left:66px;top:81px;width:59px;height:15px;border-radius:4px;background:var(--price-red);color:#fff;font-family:"Noto Serif",serif;font-size:9px;text-align:center;line-height:15px}
.listing h3{position:absolute;left:0;width:100%;top:101px;text-align:center;font-family:"Noto Serif",serif;font-weight:400;font-size:12.5px;color:var(--link-blue)}
.listing p{position:absolute;left:19px;top:125px;width:162px;font-size:7px;line-height:10px;color:var(--muted)}
.listing .view{left:58px;top:163px;width:70px;height:18px;border-radius:3px;background:linear-gradient(#fff,#e6e6e6);border:1px solid #c8c8c8;font-size:6px;font-weight:700;color:#333;text-align:center;line-height:16px;white-space:nowrap}
.featured{left:40px;top:638px;width:598px;height:169px;border:1px solid var(--line);border-radius:3px;background:linear-gradient(#f8f8f8,#e4e4e4)}
.featured .photo{top:10px;width:255px;height:126px}
.featured p{position:absolute;top:140px;width:250px;font-size:7.5px;line-height:10px;color:#555}
.gallery-main{left:54px;top:853px;width:351px;height:188px;border:2px solid #bbb;background:linear-gradient(180deg,#1b4fd0,#5a86e6 30%,#9f6a52 55%,#8a4e3a 80%,#4d7a33)}
.thumb{top:1048px;width:60px;height:52px;border:2px solid #aaa;background:linear-gradient(180deg,#6a8fc8,#7d6650 60%,#4a7a38)}
.side-box{left:425px;width:211px;border:1px solid var(--line);border-radius:3px;background:linear-gradient(#fff 40%,#ececec)}
.news-date{font-size:7.5px;color:var(--link-blue)}
.side-text{font-size:7px;line-height:9.5px;color:#555}
.read-more{font-family:"Noto Serif",serif;font-size:8px;color:var(--read-red);text-decoration:underline;white-space:nowrap}
.avatar{left:11px;width:48px;height:38px;border:1px solid #ccc;background:linear-gradient(#fafafa,#ddd 50%,#2d2d33)}
.testimonial-name{font-size:7.5px;font-weight:700;color:var(--link-blue);white-space:nowrap}
/* footer */
.site-footer{left:0;top:1145px;width:683px;height:55px;background:linear-gradient(var(--purple-deep),var(--purple))}
.footer-brand{left:30px;top:1160px;height:26px;display:flex;align-items:center;gap:7px;font-family:"Questrial",sans-serif;font-size:16px;color:#fff}
.footer-brand .mark{width:14px;height:14px;background:#fff}
.copyright{right:26px;top:1168px;font-size:7px;color:#fff;white-space:nowrap}
</style>
</head>
<body>
<header class="site-header abs">
  <div class="brand-name abs">Marisha Ashcombe</div>
  <div class="brand-role abs">Real Estate Consultant</div>
  <div class="video-cta abs">
    <div class="badge abs"></div>
    <div class="title abs">Newest Homes With Video</div>
    <div class="action abs">Click Here to Watch..</div>
  </div>
  <div class="hero abs" role="img" aria-label="Stone two-storey house under a blue sky with garden beds">
    <div class="hero-portrait abs" role="img" aria-label="Portrait of the consultant"></div>
  </div>
  <nav class="main-nav abs">
    <a class="current" style="left:17px" href="#">HOME</a>
    <a style="left:74px" href="#">BUYING</a>
    <a style="left:138px" href="#">SELLING</a>
    <a style="left:200px" href="#">CONTACT US</a>
    <a style="left:287px" href="#">NEWS</a>
    <a style="left:340px" href="#">PHOTOGRAPHY</a>
    <a style="left:438px" href="#">ABOUT ME</a>
    <span class="franchise">HLR</span>
  </nav>
</header>

<main class="content abs"></main>

<h2 class="section-title abs" style="left:40px;top:396px">Properties For Sale</h2>
<div class="arrow abs" style="left:600px;top:398px"><svg width="11" height="11" viewBox="0 0 11 11"><path d="M6.5 3 4 5.5 6.5 8" fill="none" stroke="#555" stroke-width="1.2"/></svg></div>
<div class="arrow abs" style="left:618px;top:398px"><svg width="11" height="11" viewBox="0 0 11 11"><path d="M4.5 3 7 5.5 4.5 8" fill="none" stroke="#555" stroke-width="1.2"/></svg></div>

<section class="listing-row abs">
  <article class="listing abs" style="left:0">
    <div class="photo abs" role="img" aria-label="Green timber house with veranda"></div>
    <div class="price abs">$950,000</div>
    <h3>Modern</h3>
    <p>Soluta nobis est eligendi omnis volutas assumenda est, omnise doloresed rep eldusemp. Soluta nobis omnis ....</p>
    <div class="view abs">VIEW THE LISTING</div>
  </article>
  <article class="listing abs" style="left:194px;width:201px">
    <div class="photo abs" role="img" aria-label="Green timber house with veranda"></div>
    <div class="price abs">$950,000</div>
    <h3>Traditional</h3>
    <p>Soluta nobis est eligendi omnis volutas assumenda est, omnise doloresed rep eldusemp. Soluta nobis omnis ....</p>
    <div class="view abs">VIEW THE LISTING</div>
  </article>
  <article class="listing abs" style="left:394px;width:200px">
    <div class="photo abs" role="img" aria-label="Green timber house with veranda"></div>
    <div class="price abs">$950,000</div>
    <h3>Classic</h3>
    <p>Soluta nobis est eligendi omnis volutas assumenda est, omnise doloresed rep eldusemp. Soluta nobis omnis ....</p>
    <div class="view abs">VIEW THE LISTING</div>
  </article>
</section>

<h2 class="section-title abs" style="left:41px;top:618px">Featured Property</h2>
<section class="featured abs">
  <div class="photo abs" style="left:36px;background:linear-gradient(180deg,#3a6a2c,#c8cfd2 40%,#d9d2c0 65%,#4c8a32)" role="img" aria-label="Two-storey white house among trees"></div>
  <div class="photo abs" style="left:308px;background:linear-gradient(180deg,#4a7a34,#cfc6b8 40%,#e2dccd 65%,#5d9a3a)" role="img" aria-label="Cottage with flower garden"></div>
  <p style="left:38px">Soluta nobis est eligendi omnis volutas assumenda est, omnise doloresed rep eldusemp. Soluta nobis omnis ....</p>
  <p style="left:309px">Soluta nobis est eligendi omnis volutas assumenda est, omnise doloresed rep eldusemp. Soluta nobis omnis ....</p>
</section>
<div class="arrow abs" style="left:54px;top:709px"><svg width="11" height="11" viewBox="0 0 11 11"><path d="M6.5 3 4 5.5 6.5 8" fill="none" stroke="#555" stroke-width="1.2"/></svg></div>
<div class="arrow abs" style="left:612px;top:709px"><svg width="11" height="11" viewBox="0 0 11 11"><path d="M4.5 3 7 5.5 4.5 8" fill="none" stroke="#555" stroke-width="1.2"/></svg></div>

<h2 class="section-title abs" style="left:41px;top:827px">Property Gallery</h2>
<div class="gallery-main abs" role="img" aria-label="Large brick house with dormer windows"></div>
<div class="thumb abs" style="left:64px" role="img" aria-label="House thumbnail"></div>
<div class="thumb abs" style="left:132px" role="img" aria-label="House thumbnail"></div>
<div class="thumb abs" style="left:200px" role="img" aria-label="House thumbnail"></div>
<div class="thumb abs" style="left:268px" role="img" aria-label="House thumbnail"></div>
<div class="thumb abs" style="left:336px" role="img" aria-label="House thumbnail"></div>
<div class="arrow abs" style="left:45px;top:1067px"><svg width="11" height="11" viewBox="0 0 11 11"><path d="M6.5 3 4 5.5 6.5 8" fill="none" stroke="#555" stroke-width="1.2"/></svg></div>
<div class="arrow abs" style="left:401px;top:1067px"><svg width="11" height="11" viewBox="0 0 11 11"><path d="M4.5 3 7 5.5 4.5 8" fill="none" stroke="#555" stroke-width="1.2"/></svg></div>

<h2 class="section-title abs" style="left:425px;top:827px">Latest News</h2>
<aside class="side-box abs" style="top:852px;height:108px">
  <div class="news-date abs" style="left:8px;top:7px">12-08-2011</div>
  <p class="side-text abs" style="left:8px;top:20px;width:196px">Soluta nobis est eligendi omnis volutas assumenda est, om nise doloresed rep eldusemp. Soluta n doloresed rep eldusemp. obis omnis ....</p>
  <div class="news-date abs" style="left:8px;top:54px">12-08-2011</div>
  <p class="side-text abs" style="left:8px;top:67px;width:196px">Soluta nobis est eligendi omnis volutas assumenda est, om nise doloresed rep eldusemp. Soluta n doloresed rep eldusemp. obis omnis ....</p>
  <a class="read-more abs" style="left:159px;top:92px" href="#">Read more..</a>
</aside>

<h2 class="section-title abs" style="left:425px;top:967px">Testimonials</h2>
<aside class="side-box abs" style="top:987px;height:116px">
  <div class="avatar abs" style="top:8px" role="img" aria-label="Client couple portrait"></div>
  <div class="testimonial-name abs" style="left:70px;top:10px">Volutas Assumenda</div>
  <p class="side-text abs" style="left:70px;top:21px;width:134px">Soluta nobis est eligendi omnis volutas assumenda est, om nise doloresed rep eldusemp ....</p>
  <div class="avatar abs" style="top:57px" role="img" aria-label="Client couple portrait"></div>
  <div class="testimonial-name abs" style="left:70px;top:59px">Volutas Assumenda</div>
  <p class="side-text abs" style="left:70px;top:70px;width:134px">Soluta nobis est eligendi omnis volutas assumenda est, om nise doloresed rep eldusemp....</p>
  <a class="read-more abs" style="left:159px;top:99px" href="#">Read more..</a>
</aside>

<footer class="site-footer abs"></footer>
<div class="footer-brand abs"><span class="mark"></span>HLR homes</div>
<div class="copyright abs">Copyright @ 2011 MarishaAshcombe.com. All Rights Reserved.</div>
</body>
</html>
```